Business Card Design

Cake decorating business in a small town in Australia. looking for a style that is fresh with a touch of vintage/country. liking these ideas, timber backgrounds, chalkboards, bunting, flowers and cake elements (rolling pins, cupcakes, cake stands, etc.) would consider a shot saying/statement. would like the back of the card to have wording "Specialising in delectable treats for all your special occasions" - wedding cakes - birthday cakes - special occasion cakes - novelty cakes - cupcakes, cookies, slices and cake pops. maybe incorporate a cake in design on back page. attached are a few of my favourite cakes and the start of a card design I liked.

Industry/Entity Type

Business

Contact Information for Business Card

Marigold's Sugarloft Bakes 0438 056 969Find me on (Chirpwall Logo)

Requirements
Nice to have
• timber, some of my designs, chalkboard, baking utensils
Should not have
• no red font

```html
<!DOCTYPE html>
<html lang="en">
<head>
<meta charset="utf-8">
<title>Marigold's Sugarloft Bakes – Business Card</title>
<link href="https://fonts.googleapis.com/css2?family=Playfair+Display:wght@400&family=Roboto:wght@300;400&display=swap" rel="stylesheet">
<style>
  :root {
    --page: #e7e4df;
    --card: #ffffff;
    --card-shade: #f1f1f1;
    --ink: #1c1c1c;
    --accent: #45a7e0;
    --icon: #2f7fd0;
    --timber-light: #b7a590;
    --timber-dark: #7e6c5a;
    --cake-green: #b9d83a;
    --cake-blue: #7cc3ea;
  }
  * { box-sizing: border-box; margin: 0; padding: 0; }
  html, body {
    width: 1200px; height: 892px; overflow: hidden;
    background: var(--page);
  }
  .sheet {
    width: 1200px; height: 892px;
    display: flex; flex-direction: column; align-items: center; justify-content: center;
    gap: 40px;
  }
  .card {
    width: 700px; height: 400px;
    background: linear-gradient(180deg, var(--card) 60%, var(--card-shade));
    box-shadow: 0 6px 18px rgba(0,0,0,.18);
    position: relative; overflow: hidden;
  }

  /* Front */
  .card-front { display: flex; }
  .front-photo {
    width: 290px; height: 100%;
    background:
      radial-gradient(ellipse 55% 40% at 50% 55%, var(--cake-green) 0 45%, var(--cake-blue) 46% 60%, transparent 61%),
      linear-gradient(90deg, var(--timber-light), var(--timber-dark) 50%, var(--timber-light));
  }
  .front-info {
    flex: 1; position: relative;
    font-family: "Roboto", Arial, sans-serif; color: var(--ink);
  }
  .front-brand {
    position: absolute; left: 26px; top: 26px;
    font-family: "Playfair Display", Georgia, serif; font-size: 30px; font-weight: 400;
  }
  .front-person { position: absolute; right: 28px; top: 118px; text-align: right; }
  .person-name {
    font-family: "Playfair Display", Georgia, serif; font-size: 32px; color: var(--accent);
  }
  .person-role { font-size: 18px; margin-top: 2px; }
  .contact-list {
    position: absolute; right: 24px; bottom: 26px;
    list-style: none; text-align: right; font-size: 17px; line-height: 29px;
  }
  .contact-list li { display: flex; justify-content: flex-end; align-items: center; gap: 10px; }
  .contact-icon {
    width: 16px; height: 16px; background: var(--icon); display: inline-flex;
    align-items: center; justify-content: center; flex: none;
  }
  .contact-icon svg { width: 12px; height: 12px; }

  /* Back */
  .card-back { padding: 44px 50px; }
  .back-brand {
    font-family: "Playfair Display", Georgia, serif; font-size: 50px; font-weight: 400;
    color: var(--ink); text-align: center;
    padding-bottom: 14px; border-bottom: 2px solid var(--ink);
  }
  .service-list {
    list-style: none; margin-top: 22px;
    font-family: "Roboto", Arial, sans-serif; font-weight: 300; font-size: 20px; line-height: 31px;
    color: var(--ink); text-align: left; padding-left: 40px;
  }
</style>
</head>
<body>
<main class="sheet">
  <section class="card card-front">
    <div class="front-photo" role="img" aria-label="Photo of a decorated two-tier birthday cake on a timber table"></div>
    <div class="front-info">
      <h1 class="front-brand">Marigold's Sugarloft Bakes</h1>
      <div class="front-person">
        <p class="person-name">Pia Calloway</p>
        <p class="person-role">Manager</p>
      </div>
      <ul class="contact-list">
        <li>0417 382 254
          <span class="contact-icon"><svg viewBox="0 0 12 12"><path d="M3 1l2 2-1 1.5c.6 1.4 1.6 2.4 3 3L8.5 6.5l2 2L9 10.5C5 10 2 7 1.5 3z" fill="#fff"/></svg></span></li>
        <li>Find me on Chirpwall
          <span class="contact-icon"></span></li>
        <li>hello@sugarloftbakes.com
          <span class="contact-icon"><svg viewBox="0 0 12 12"><rect x="1.5" y="3" width="9" height="6" fill="none" stroke="#fff"/><path d="M1.5 3l4.5 3.5L10.5 3" fill="none" stroke="#fff"/></svg></span></li>
        <li>www.sugarloftbakes.com
          <span class="contact-icon"><svg viewBox="0 0 12 12"><circle cx="6" cy="6" r="4.2" fill="none" stroke="#fff"/><path d="M1.8 6h8.4M6 1.8c-2 2.5-2 5.9 0 8.4M6 1.8c2 2.5 2 5.9 0 8.4" fill="none" stroke="#fff" stroke-width=".8"/></svg></span></li>
        <li>18 Wattle Row Bellbrook, NSW 2440
          <span class="contact-icon"><svg viewBox="0 0 12 12"><path d="M6 11S2.5 7 2.5 4.6a3.5 3.5 0 0 1 7 0C9.5 7 6 11 6 11z" fill="#fff"/><circle cx="6" cy="4.6" r="1.2" fill="var(--icon)"/></svg></span></li>
      </ul>
    </div>
  </section>

  <section class="card card-back">
    <h2 class="back-brand">Marigold's Sugarloft Bakes</h2>
    <ul class="service-list">
      <li>wedding cakes</li>
      <li>birthday cakes</li>
      <li>special occasion cakes</li>
      <li>novelty cakes</li>
      <li>cupcakes</li>
      <li>cookies</li>
      <li>slices and cake pops</li>
    </ul>
  </section>
</main>
</body>
</html>
```